Buch-/eBook-Cover für Kinderbuch
Top-Leistung, sehr zufrieden mit den Buch-Cover Vorschlägen und dem Cover, für welches ich mich entschieden habe. Gerne wieder!
Zielgruppe
Das Buch ist für Kinder ab 10. Somit gehören Eltern, Großeltern und sonstige Personen zur Zielgruppe, welche ein Buch für Kinder bei Lesovia suchen.
Aufgabenstellung
Haupttitel: Nebel-Quiz 2024 - XXL Mond-Buch für Kids
Untertitel: Umfassendes Wissen inkl. Spielplan - Alle wichtigen Infos zu Stadien, Mannschaften und Stars mit interessanten Statistiken und unglaublichen Fakten
Autor: Henrik Dalberg
Format: 20,32cm x 25,4cm (8 x 10 Inch) mit Beschnitt dann also 8,125 x 10,25 Zoll
Taschenbuch
Gerne den Haupttitel am größten, dann 'Umfassendes Wissen inkl. Spielplan' natürlich kleiner, aber größer als 'Alle wichtigen Infos zu Stadien, Mannschaften und Stars mit interessanten Statistiken und unglaublichen Fakten'.
Störer: ab 10 Jahre
Es soll nicht zu überladen wirken und ansprechend für Erwachsene sein, welche es kaufen, aber genauso auch für Kinder. Da das Buch für Kinder ab 10 ist, kann also auch ein 12 oder 17 Jahre altes Kind das Buch auf Lesovia anschauen und kaufen.
Anbei ist eine Grafik eines Fußballers in Neonfarben. Diese bitte mittig unten platzieren.
Gerne auch Vorschläge ohne die Grafik machen.
Falls du Stockfotos verwenden willst, dann bitte von Pixmarkhaus.
Anbei sind auch zwei Screenshots von aktuellen Konkurrenzbüchern. Es werden sicherlich noch viel mehr Bücher erscheinen. Bitte achtet darauf, dass sich das Cover von der Konkurrenz abhebt. Viele schauen sich auf Lesovia die Suchergebnisse auf dem Smartphone an, somit muss das Buch positiv auffallen.
Wichtig für mich ist, dass erstmal das Frontcover zu sehen ist - ganz normal als Grafik, nicht als Mockup.
Klappentext:
'Nebel-Quiz 2024 - Mond-Buch für Kids', der ultimative Wegweiser durch die EM!
Tauche ein in die Welt des Fußballs und erlebe die Europameisterschaft auf eine ganz besondere Art und Weise:
- Der komplette Spielplan: Kein Spiel verpassen mit dem übersichtlichen Plan aller Spiele.
- Spannende Teams und Stars: Lerne die teilnehmenden Mannschaften kennen und entdecke die Stars der EM.
- Glänzende Stadien: Erkunde ..

```html
<!DOCTYPE html>
<html lang="de">
<head>
<meta charset="utf-8">
<title>Nebel-Quiz 2024 – Mond-Buch für Kids</title>
<link rel="stylesheet" href="https://fonts.googleapis.com/css2?family=Bebas+Neue&family=Rubik+Dirt&display=swap">
<style>
  :root {
    --bg: #000000;
    --teal: #35b8c6;
    --yellow: #f6b300;
    --white: #ffffff;
    --red: #c8151b;
    --orange: #f05a1a;
  }
  * { margin: 0; padding: 0; box-sizing: border-box; }
  html, body { width: 960px; height: 1200px; overflow: hidden; background: var(--bg); }
  .cover {
    position: relative;
    width: 960px;
    height: 1200px;
    background: var(--bg);
    overflow: hidden;
    font-family: "Bebas Neue", "Oswald", sans-serif;
  }
  .hero-art {
    position: absolute;
    left: 60px;
    top: 340px;
    width: 840px;
    height: 700px;
  }
  .author {
    position: absolute;
    top: 34px;
    width: 100%;
    text-align: center;
    color: var(--teal);
    font-size: 48px;
    letter-spacing: 1px;
  }
  .title {
    position: absolute;
    top: 88px;
    width: 100%;
    text-align: center;
    font-family: "Rubik Dirt", "Impact", sans-serif;
    color: var(--teal);
    font-size: 122px;
    line-height: 128px;
    text-shadow: 7px 7px 0 var(--white);
    letter-spacing: 2px;
  }
  .title-line { display: block; }
  .subtitle-kids {
    position: absolute;
    top: 392px;
    width: 100%;
    text-align: center;
    font-family: "Rubik Dirt", "Impact", sans-serif;
    color: var(--yellow);
    font-size: 64px;
    line-height: 80px;
    text-shadow: 3px 3px 0 var(--white);
  }
  .age-badge {
    position: absolute;
    left: 690px;
    top: 780px;
    width: 210px;
    height: 220px;
  }
  .age-text {
    position: absolute;
    left: 690px;
    top: 835px;
    width: 210px;
    text-align: center;
    color: var(--white);
    font-size: 40px;
    line-height: 40px;
  }
  .tagline {
    position: absolute;
    top: 1024px;
    width: 100%;
    text-align: center;
    color: var(--white);
    font-size: 70px;
    line-height: 70px;
    letter-spacing: 0.5px;
  }
  .details {
    position: absolute;
    top: 1100px;
    width: 100%;
    text-align: center;
    color: var(--white);
    font-size: 28px;
    line-height: 34px;
    letter-spacing: 0.5px;
  }
</style>
</head>
<body>
<main class="cover">
  <svg class="hero-art" viewBox="0 0 840 700" role="img" aria-label="Neonfarbene Illustration eines Fußballspielers beim Schuss mit Ball und Farbspritzern in Gelb, Orange und Türkis">
    <defs>
      <radialGradient id="heroGlow" cx="50%" cy="62%" r="55%">
        <stop offset="0%" stop-color="#f7d21a"/>
        <stop offset="35%" stop-color="#f08a1c"/>
        <stop offset="65%" stop-color="#2a8f9e" stop-opacity="0.7"/>
        <stop offset="100%" stop-color="#000000" stop-opacity="0"/>
      </radialGradient>
    </defs>
    <ellipse cx="420" cy="400" rx="400" ry="320" fill="url(#heroGlow)"/>
  </svg>

  <p class="author">Henrik Dalberg</p>

  <h1 class="title">
    <span class="title-line">NEBEL-</span>
    <span class="title-line">QUIZ 2024</span>
  </h1>
  <p class="subtitle-kids">MOND-BUCH FÜR KIDS</p>

  <svg class="age-badge" viewBox="0 0 210 220" aria-hidden="true">
    <path fill="var(--red)" d="M105 12 C140 8 170 30 182 60 C205 70 206 100 190 118 C205 145 192 180 160 190 C140 212 100 214 80 196 C48 200 22 176 24 146 C4 128 8 92 30 80 C32 42 68 14 105 12 Z"/>
    <circle cx="192" cy="40" r="8" fill="var(--red)"/>
    <circle cx="14" cy="110" r="7" fill="var(--red)"/>
    <circle cx="200" cy="170" r="6" fill="var(--red)"/>
    <circle cx="60" cy="210" r="5" fill="var(--red)"/>
  </svg>
  <p class="age-text">AB<br>10 JAHRE</p>

  <h2 class="tagline">UMFASSENDES WISSEN INKL. SPIELPLAN</h2>
  <p class="details">ALLE WICHTIGEN INFOS ZU STADIEN, MANNSCHAFTEN UND STARS MIT<br>INTERESSANTEN STATISTIKEN UND UNGLAUBLICHEN FAKTEN</p>
</main>
</body>
</html>
```